Spiritual Healing bussiness needs logo/business card

Simple, clean looking logo/card
For spiritual business with healing services and occult rituals

Contact Information for Business Card

Needs my name: Tovin Harlowe
Business name: Velka Healing Shop
Services provided and worded in this way:

Reiki Healing
Tarot
Oils
Rituals Of Change

Can look occult like but with light energy.

Colors
0255a3
3276b5
85abd2
33a6d7
85cae6
0292cd

```html
<!DOCTYPE html>
<html lang="en">
<head>
<meta charset="utf-8">
<title>Velka Healing Shop – Business Cards</title>
<link href="https://fonts.googleapis.com/css2?family=Federo&display=swap" rel="stylesheet">
<style>
  :root {
    --board-light: #ececec;
    --board-dark: #7d7b7c;
    --card-bg: #eaf5fb;
    --rose: #d9527a;
    --rose-1: #e8ccdc;
    --rose-2: #f1e3f2;
    --rose-3: #f0ebea;
    --rose-mark: #f3b4cf;
    --blue: #0255a3;
    --blue-1: #bdd6eb;
    --blue-2: #cde1f1;
    --blue-3: #d8ebf5;
    --blue-mark: #85abd2;
  }
  * { margin: 0; padding: 0; box-sizing: border-box; }
  html, body { width: 1200px; height: 1200px; overflow: hidden; }
  body {
    position: relative;
    background: radial-gradient(ellipse 60% 55% at 50% 62%, var(--board-light) 0%, #bdbbbc 55%, var(--board-dark) 100%);
    font-family: "Federo", sans-serif;
  }
  .card {
    position: absolute;
    width: 496px;
    height: 321px;
    background: var(--card-bg);
    overflow: hidden;
  }
  .card--front-rose { left: 98px;  top: 61px; }
  .card--front-blue { left: 607px; top: 61px; }
  .card--back-rose  { left: 98px;  top: 395px; }
  .card--back-blue  { left: 607px; top: 395px; }
  .card__backdrop { position: absolute; inset: 0; width: 100%; height: 100%; }
  .card--rose { color: var(--rose); }
  .card--blue { color: var(--blue); }
  .card--rose .tone-1 { fill: var(--rose-1); }
  .card--rose .tone-2 { fill: var(--rose-2); }
  .card--rose .tone-3 { fill: var(--rose-3); }
  .card--rose .mark   { fill: var(--rose-mark); }
  .card--blue .tone-1 { fill: var(--blue-1); }
  .card--blue .tone-2 { fill: var(--blue-2); }
  .card--blue .tone-3 { fill: var(--blue-3); }
  .card--blue .mark   { fill: var(--blue-mark); }
  .brand-name {
    position: absolute;
    white-space: nowrap;
    line-height: 1;
  }
  .brand-name--front {
    left: 0; right: 0;
    top: 207px;
    text-align: center;
    font-size: 31px;
  }
  .brand-name--header {
    left: 109px;
    top: 29px;
    font-size: 25px;
  }
  .holder-name {
    position: absolute;
    left: 56px;
    top: 148px;
    font-size: 30px;
    line-height: 1;
    white-space: nowrap;
  }
  .services {
    position: absolute;
    left: 280px;
    width: 160px;
    top: 138px;
    list-style: none;
    text-align: center;
    font-size: 22px;
    line-height: 40px;
    white-space: nowrap;
  }
</style>
</head>
<body>

  <!-- Front, rose -->
  <section class="card card--front-rose card--rose">
    <svg class="card__backdrop" viewBox="0 0 496 321" aria-hidden="true">
      <circle class="tone-1" cx="420" cy="340" r="420"/>
      <circle class="tone-2" cx="470" cy="420" r="410"/>
      <circle class="tone-3" cx="420" cy="560" r="380"/>
      <circle class="mark" cx="248" cy="122" r="52"/>
    </svg>
    <div class="brand-name brand-name--front">Velka Healing Shop</div>
  </section>

  <!-- Front, blue -->
  <section class="card card--front-blue card--blue">
    <svg class="card__backdrop" viewBox="0 0 496 321" aria-hidden="true">
      <circle class="tone-1" cx="420" cy="340" r="420"/>
      <circle class="tone-2" cx="470" cy="420" r="410"/>
      <circle class="tone-3" cx="420" cy="560" r="380"/>
      <circle class="mark" cx="248" cy="122" r="52"/>
    </svg>
    <div class="brand-name brand-name--front">Velka Healing Shop</div>
  </section>

  <!-- Back, rose -->
  <section class="card card--back-rose card--rose">
    <svg class="card__backdrop" viewBox="0 0 496 321" aria-hidden="true">
      <circle class="tone-1" cx="140" cy="440" r="420"/>
      <circle class="tone-2" cx="110" cy="470" r="390"/>
      <circle class="tone-3" cx="120" cy="560" r="400"/>
      <circle class="mark" cx="58" cy="53" r="22"/>
    </svg>
    <div class="brand-name brand-name--header">Velka Healing Shop</div>
    <div class="holder-name">Tovin Harlowe</div>
    <ul class="services">
      <li>Reiki Healing</li>
      <li>Tarot</li>
      <li>Oils</li>
      <li>Rituals Of Change</li>
    </ul>
  </section>

  <!-- Back, blue -->
  <section class="card card--back-blue card--blue">
    <svg class="card__backdrop" viewBox="0 0 496 321" aria-hidden="true">
      <circle class="tone-1" cx="140" cy="440" r="420"/>
      <circle class="tone-2" cx="110" cy="470" r="390"/>
      <circle class="tone-3" cx="120" cy="560" r="400"/>
      <circle class="mark" cx="58" cy="53" r="22"/>
    </svg>
    <div class="brand-name brand-name--header">Velka Healing Shop</div>
    <div class="holder-name">Tovin Harlowe</div>
    <ul class="services">
      <li>Reiki Healing</li>
      <li>Tarot</li>
      <li>Oils</li>
      <li>Rituals Of Change</li>
    </ul>
  </section>

</body>
</html>
```